Dalvorn-Ke Photography needs a poster for a upcoming event

We need a Music Concert Poster designed for a musician named Marc T. Lindow. The concert is happening 6:30 pm, Saturday, January 10, 2015 Look to our current design ideas for inspiration. Keep it clean and simple but I want to see your creative ideas. Please view the throw togethers screenshots I have included in this project and then use one of the clean images in your design. Visit www.pinboardia.example/marclind/concert-posters/ for the musicians favorite music posters and gather ideas from there as well.

Industry/Entity Type

Event

Requirements
Nice to have
• Lets tend to lean towards a more sanserif font

```html
<!DOCTYPE html>
<html lang="en">
<head>
<meta charset="utf-8">
<title>Marc T. Lindow — Concert Poster</title>
<link rel="stylesheet" href="https://fonts.googleapis.com/css2?family=Montserrat:wght@300;600;700&display=swap">
<style>
  :root {
    --paper: #f4f4f4;
    --ink-date: #3a3a3a;
    --ink-venue: #8c8c8c;
    --accent-red: #d1343a;
    --band-light: #e2e2e2;
    --band-mid: #c9c9c9;
    --letter-dark: #2b2b2b;
    --letter-mid: #6a6a6a;
    --name-white: #ffffff;
  }
  html, body {
    margin: 0;
    padding: 0;
    width: 873px;
    height: 1200px;
    overflow: hidden;
    background: var(--paper);
  }
  .poster {
    position: relative;
    width: 873px;
    height: 1200px;
    background: var(--paper);
    font-family: "Montserrat", "Helvetica Neue", Arial, sans-serif;
  }
  .event-time {
    position: absolute;
    left: 91px;
    top: 114px;
    margin: 0;
    font-weight: 300;
    font-size: 34px;
    line-height: 43px;
    color: var(--ink-date);
  }
  .venue {
    position: absolute;
    right: 91px;
    top: 52px;
    margin: 0;
    text-align: right;
    font-style: normal;
    font-weight: 600;
    font-size: 24px;
    line-height: 34px;
    color: var(--ink-venue);
  }
  .admission {
    position: absolute;
    right: 91px;
    top: 199px;
    margin: 0;
    font-weight: 700;
    font-size: 32px;
    letter-spacing: 0.5px;
    color: var(--accent-red);
  }
  .feature {
    position: absolute;
    left: 0;
    top: 0;
    width: 873px;
    height: 1200px;
  }
  .performer {
    font-family: "Montserrat", "Helvetica Neue", Arial, sans-serif;
    font-weight: 700;
    font-size: 60px;
    letter-spacing: 1px;
    fill: var(--name-white);
  }
  .monogram {
    font-family: "Montserrat", "Helvetica Neue", Arial, sans-serif;
    font-weight: 700;
  }
</style>
</head>
<body>
<main class="poster">
  <p class="event-time">January 10<br>Saturday<br>6:30 PM</p>

  <address class="venue">
    Harbor Point SDA Church<br>
    214 Linden Cove Ave.<br>
    Harbor Point<br>
    FL, 32990
  </address>
  <p class="admission">FREE ENTRANCE!</p>

  <svg class="feature" viewBox="0 0 873 1200" width="873" height="1200">
    <defs>
      <linearGradient id="band-tone" x1="0" y1="0" x2="1" y2="1">
        <stop offset="0" stop-color="var(--band-mid)"/>
        <stop offset="0.5" stop-color="var(--band-light)"/>
        <stop offset="1" stop-color="var(--band-mid)"/>
      </linearGradient>
      <linearGradient id="letter-tone" x1="0" y1="0" x2="0.6" y2="1">
        <stop offset="0" stop-color="var(--letter-dark)"/>
        <stop offset="0.45" stop-color="var(--letter-mid)"/>
        <stop offset="1" stop-color="var(--letter-dark)"/>
      </linearGradient>
    </defs>

    <rect class="photo-band" x="0" y="340" width="873" height="760" fill="url(#band-tone)"
          role="img" aria-label="Soft-focus black and white portrait of the musician holding a violin bow"/>

    <text class="monogram" x="175" y="1120" font-size="1160" textLength="648" lengthAdjust="spacingAndGlyphs"
          fill="url(#letter-tone)" role="img" aria-label="Large letter M filled with a black and white photo of the musician">M</text>

    <text class="performer" x="205" y="1041">MARC T. LINDOW</text>
  </svg>
</main>
</body>
</html>
```